Simple Business Card Design for Foodie

Job:

Make a very simple, minimalist business card design with my details including adjusted logo. One side to be white (with logo & text). Other side to be yellow - try plain or with logo (or part of logo eg Z). Need business card to have continuity with website.

Logo:
Our logo is made from a free download font website:
http://www.typegrotto.net/search.php?q=rubber
but the spacing/kerning needs correcting/adjusting as the font spaces unevenly between letters (see attached files). Need logo to be very crisp/sharp when printed.

Printing:
We will be using Kelvo.com so the design needs to conform to their requirements, see here:

http://uk.kelvo.com/products/velour/business-cards.html (scroll down for dimensions and guidelines)

Design:

must say "plant-based food consulting" underneath logo or somewhere
no address needed in contact section
sharp corners (not rounded)
one side white, one side yellow

name: Harriet Colwick
1xmobile number: +44 7700900461
1xtwiiter: @pelkoadvice
website address www.marrowlanekitchen.com
email address pelko@marrowlanekitchen.com

Should be easy quick job, prompt + detailed feedback given, am online in UK 9am-10pm for next 3 days. Website is www.marrowlanekitchen.com

Industry/Entity Type

Business

Requirements
Must have
• The logo must be corrected. The kerning is not right.

Please use a warm-grey for text

Please submit in matt format, we will be printing matt finish.

Should not have
• Avoid using banners or curvy highlights

Please avoid using black

Please avoid submitting in gloss finish

```html
<!DOCTYPE html>
<html lang="en">
<head>
<meta charset="utf-8">
<title>Pelko business card</title>
<link rel="stylesheet" href="https://fonts.googleapis.com/css2?family=Cinzel:wght@400;600;700&display=swap">
<style>
  :root {
    --backdrop: #e8e8e7;
    --card-white: #ffffff;
    --lemon-light: #f7f08e;
    --lemon-deep: #efdf48;
    --lemon-mark: #f0df52;
    --warm-grey: #5f5c58;
    --edge: #d6d6d4;
  }
  * { margin: 0; padding: 0; box-sizing: border-box; }
  html, body {
    width: 1200px;
    height: 720px;
    overflow: hidden;
    background: var(--backdrop);
  }
  .canvas {
    position: relative;
    width: 1200px;
    height: 720px;
    font-family: "Cinzel", Georgia, serif;
    color: var(--warm-grey);
  }
  .card {
    position: absolute;
    top: 242px;
    width: 420px;
    height: 238px;
    border: 1px solid var(--edge);
  }
  .card-front {
    left: 147px;
    background: var(--card-white);
  }
  .card-back {
    left: 633px;
    background: linear-gradient(135deg, var(--lemon-light), var(--lemon-deep));
    border-color: transparent;
  }
  .wordmark {
    position: absolute;
    font-weight: 700;
    line-height: 1;
    letter-spacing: 2px;
  }
  .card-front .wordmark {
    left: 22px;
    top: 24px;
    font-size: 50px;
    color: var(--lemon-mark);
  }
  .card-back .wordmark {
    left: 0;
    right: 0;
    top: 72px;
    text-align: center;
    font-size: 66px;
    color: var(--warm-grey);
  }
  .tagline {
    position: absolute;
    left: 0;
    right: 0;
    top: 150px;
    text-align: center;
    font-size: 12.5px;
    font-weight: 700;
    letter-spacing: 0.3px;
  }
  .contact-list {
    position: absolute;
    left: 22px;
    top: 170px;
    list-style: none;
  }
  .contact-list li {
    display: flex;
    align-items: center;
    height: 12px;
    font-size: 9.6px;
    line-height: 12px;
  }
  .contact-list svg {
    width: 11px;
    height: 9px;
    margin-right: 7px;
    fill: var(--warm-grey);
  }
  .holder-name {
    position: absolute;
    right: 17px;
    top: 205px;
    font-size: 13.5px;
    font-weight: 700;
  }
</style>
</head>
<body>
<main class="canvas">
  <section class="card card-front" aria-label="Card front">
    <div class="wordmark">PELKO</div>
    <ul class="contact-list">
      <li>
        <svg viewBox="0 0 11 9" aria-hidden="true"><path d="M0 3 C2 0 9 0 11 3 L9 4 L8 2.5 L3 2.5 L2 4 Z M2.5 4.5 L8.5 4.5 L10 9 L1 9 Z"/></svg>
        +44 7700900461
      </li>
      <li>
        <svg viewBox="0 0 11 9" aria-hidden="true"><path d="M0 0 H11 V9 H0 Z M1 1.2 L5.5 5 L10 1.2 Z" fill-rule="evenodd"/></svg>
        pelko@marrowlanekitchen.com
      </li>
      <li>
        <svg viewBox="0 0 11 9" aria-hidden="true"><rect x="1" y="0" width="9" height="9"/></svg>
        @pelkoadvice
      </li>
      <li>
        <svg viewBox="0 0 11 9" aria-hidden="true"><path d="M0 0 H11 V6.5 H0 Z M1.2 1.2 V5.3 H9.8 V1.2 Z M4.5 6.5 H6.5 V8 H8 V9 H3 V8 H4.5 Z" fill-rule="evenodd"/></svg>
        www.marrowlanekitchen.com
      </li>
    </ul>
    <div class="holder-name">Harriet Colwick</div>
  </section>

  <section class="card card-back" aria-label="Card back">
    <div class="wordmark">PELKO</div>
    <div class="tagline">PLANT-BASED FOOD CONSULTING</div>
  </section>
</main>
</body>
</html>
```